RJ Heating & Cooling / 2018 Varden Kestrel Medium Roof / 148"wb

Customer is looking for a new design on his new 2018 varden kestrel medium roof 148"wb van. This will be a Full Wrap.

Attached is: >Customers logo
> Template for the van he has (You don't have to use this exact one for the proof)

Please include: > Slogan- Quality work at reasonable prices
>(555) 014-2293
>Services- Repairs, installation, maintenance, water heaters, indoor air quality
>Residential & Commercial

```html
<!DOCTYPE html>
<html lang="en">
<head>
<meta charset="utf-8">
<title>RJ Heating &amp; Cooling – Van Wrap Layout</title>
<link rel="stylesheet" href="https://fonts.googleapis.com/css2?family=Oswald:wght@700&family=Nunito:ital,wght@0,900;1,800&display=swap">
<style>
  :root {
    --bg: #e3e3e3;
    --van-grey: #c9c9c9;
    --wrap-blue: #2f4a8f;
    --wrap-red: #e0232e;
    --accent-yellow: #f7c51e;
    --accent-cream: #fde9a6;
    --accent-orange: #f08a1c;
    --flame-red: #d92a1a;
    --white: #ffffff;
  }
  html, body {
    margin: 0;
    padding: 0;
    width: 1200px;
    height: 2411px;
    overflow: hidden;
    background: var(--bg);
  }
  .canvas { position: relative; width: 1200px; height: 2411px; }
  .panel { position: absolute; display: block; }
  .panel--driver { left: 50px; top: 90px; width: 1100px; height: 500px; }
  .panel--passenger { left: 50px; top: 760px; width: 1100px; height: 500px; }
  .panel--rear { left: 280px; top: 1440px; width: 640px; height: 720px; }

  .van-body { fill: var(--van-grey); }
  .wrap-blue { fill: var(--wrap-blue); }
  .wrap-red { fill: var(--wrap-red); }
  .rocker-stripe { fill: var(--accent-orange); }

  .web-address {
    font-family: "Nunito", sans-serif; font-style: italic; font-weight: 800;
    fill: var(--accent-cream);
  }
  .slogan {
    font-family: "Oswald", sans-serif; font-weight: 700;
    fill: var(--wrap-red); stroke: var(--white); stroke-width: 6;
    paint-order: stroke; letter-spacing: -0.5px;
  }
  .brand-name {
    font-family: "Nunito", sans-serif; font-weight: 900;
    fill: var(--white);
  }
  .brand-dot { fill: var(--accent-yellow); }
  .phone, .services, .badge-sub {
    font-family: "Nunito", sans-serif; font-style: italic; font-weight: 800;
  }
  .phone { fill: var(--accent-cream); }
  .services { fill: var(--accent-cream); }
  .badge-hours {
    font-family: "Nunito", sans-serif; font-style: italic; font-weight: 900;
    fill: var(--accent-yellow);
  }
  .badge-sub--orange { fill: var(--accent-orange); }
  .badge-sub--yellow { fill: var(--accent-yellow); }
  .badge-rule { stroke: var(--accent-yellow); stroke-width: 5; }
  .rear-slogan {
    font-family: "Nunito", sans-serif; font-style: italic; font-weight: 800;
    fill: var(--accent-cream);
  }
  .market-label {
    font-family: "Nunito", sans-serif; font-style: italic; font-weight: 900;
    fill: var(--white);
  }
</style>
</head>
<body>
<main class="canvas">

  <!-- Driver side: cab on the left -->
  <svg class="panel panel--driver" viewBox="0 0 1100 500" aria-label="Driver side wrap panel">
    <path class="van-body" d="M10,420 L12,330 Q20,280 110,250 L260,110 Q300,80 380,72 L780,40 L1050,20 L1060,420 Q900,425 860,420 Q820,350 760,350 Q700,350 680,420 L300,420 Q280,360 210,360 Q140,360 120,420 Z"/>
    <path class="wrap-blue" d="M232,420 L236,330 Q240,300 280,300 L360,300 L372,118 Q376,100 400,98 L575,95 L1050,75 L1060,410 Q900,412 860,410 Q820,350 760,350 Q700,350 680,412 L300,415 Z"/>
    <path class="wrap-red" d="M570,100 Q600,25 650,12 L1045,0 L1052,78 Q800,82 570,100 Z"/>
    <rect class="rocker-stripe" x="245" y="455" width="530" height="22" transform="skewX(-2)"/>

    <text class="web-address" x="1020" y="45" font-size="26" text-anchor="end">rjheatingandcooling.com</text>

    <text class="slogan" font-size="46" text-anchor="middle">
      <tspan x="525" y="140">Quality Work</tspan>
      <tspan x="525" y="184">at Reasonable</tspan>
      <tspan x="525" y="228">Prices</tspan>
    </text>

    <circle class="brand-dot" cx="670" cy="150" r="14"/>
    <text class="brand-name" font-size="52">
      <tspan x="695" y="135">RJ Heating</tspan>
      <tspan x="720" y="190">&amp; Cooling</tspan>
    </text>

    <text class="badge-hours" x="232" y="292" font-size="50">24/7</text>
    <text class="badge-sub badge-sub--orange" x="230" y="318" font-size="20">Emergency</text>
    <text class="badge-sub badge-sub--yellow" x="236" y="340" font-size="18">Support</text>
    <line class="badge-rule" x1="310" y1="334" x2="380" y2="332"/>

    <text class="phone" x="410" y="310" font-size="32">(555) 014-2293</text>

    <text class="services" font-size="19" text-anchor="middle">
      <tspan x="870" y="280">Repairs | Installation | Maintenance</tspan>
      <tspan x="870" y="305">Water heaters | Indoor air quality</tspan>
    </text>
  </svg>

  <!-- Passenger side: cab on the right -->
  <svg class="panel panel--passenger" viewBox="0 0 1100 500" aria-label="Passenger side wrap panel">
    <g transform="translate(1100,0) scale(-1,1)">
      <path class="van-body" d="M10,420 L12,330 Q20,280 110,250 L260,110 Q300,80 380,72 L780,40 L1050,20 L1060,420 Q900,425 860,420 Q820,350 760,350 Q700,350 680,420 L300,420 Q280,360 210,360 Q140,360 120,420 Z"/>
      <path class="wrap-blue" d="M232,420 L236,330 Q240,300 280,300 L360,300 L372,118 Q376,100 400,98 L575,95 L1050,75 L1060,410 Q900,412 860,410 Q820,350 760,350 Q700,350 680,412 L300,415 Z"/>
      <path class="wrap-red" d="M570,100 Q600,25 650,12 L1045,0 L1052,78 Q800,82 570,100 Z"/>
      <rect class="rocker-stripe" x="245" y="455" width="530" height="22" transform="skewX(-2)"/>
    </g>

    <text class="web-address" x="70" y="45" font-size="26">rjheatingandcooling.com</text>

    <circle class="brand-dot" cx="62" cy="150" r="14"/>
    <text class="brand-name" font-size="52">
      <tspan x="87" y="135">RJ Heating</tspan>
      <tspan x="112" y="190">&amp; Cooling</tspan>
    </text>

    <text class="slogan" font-size="46" text-anchor="middle">
      <tspan x="575" y="140">Quality Work</tspan>
      <tspan x="575" y="184">at Reasonable</tspan>
      <tspan x="575" y="228">Prices</tspan>
    </text>

    <text class="services" font-size="19" text-anchor="middle">
      <tspan x="230" y="280">Repairs | Installation | Maintenance</tspan>
      <tspan x="230" y="305">Water heaters | Indoor air quality</tspan>
    </text>

    <text class="phone" x="440" y="310" font-size="32">(555) 014-2293</text>

    <text class="badge-hours" x="720" y="292" font-size="50">24/7</text>
    <text class="badge-sub badge-sub--orange" x="718" y="318" font-size="20">Emergency</text>
    <text class="badge-sub badge-sub--yellow" x="724" y="340" font-size="18">Support</text>
    <line class="badge-rule" x1="798" y1="334" x2="868" y2="332"/>
  </svg>

  <!-- Rear doors -->
  <svg class="panel panel--rear" viewBox="0 0 640 720" aria-label="Rear door wrap panel">
    <defs>
      <linearGradient id="flameGlow" x1="0" y1="0" x2="0" y2="1">
        <stop offset="0" stop-color="#f7a21c" stop-opacity="0"/>
        <stop offset="0.5" stop-color="#f07a1c"/>
        <stop offset="1" stop-color="#d92a1a"/>
      </linearGradient>
      <linearGradient id="mascotTones" x1="0" y1="0" x2="0" y2="1">
        <stop offset="0" stop-color="#d8332b"/>
        <stop offset="0.45" stop-color="#3a6fc4"/>
        <stop offset="1" stop-color="#2a3f7a"/>
      </linearGradient>
    </defs>
    <path class="wrap-blue" d="M20,40 Q22,10 60,8 L580,8 Q618,10 620,40 L628,420 Q604,445 630,470 L622,712 L18,712 L10,470 Q36,445 12,420 Z"/>
    <path class="wrap-red" d="M20,40 Q22,10 60,8 L580,8 Q618,10 620,40 L622,118 L18,118 Z"/>

    <text class="rear-slogan" font-size="36" text-anchor="middle">
      <tspan x="320" y="62">Quality Work at</tspan>
      <tspan x="320" y="102">Reasonable Prices</tspan>
    </text>

    <circle class="brand-dot" cx="70" cy="175" r="14"/>
    <text class="brand-name" font-size="60">
      <tspan x="98" y="190">RJ Heating</tspan>
      <tspan x="130" y="255">&amp; Cooling</tspan>
    </text>

    <rect x="0" y="600" width="640" height="112" fill="url(#flameGlow)" role="img" aria-label="Flame artwork along the bottom of the doors"/>

    <text class="badge-hours" x="70" y="340" font-size="50">24/7</text>
    <text class="badge-sub badge-sub--orange" x="70" y="362" font-size="18">Emergency</text>
    <text class="badge-sub badge-sub--yellow" x="150" y="378" font-size="18" transform="rotate(-18 150 378)">Support</text>
    <line class="badge-rule" x1="60" y1="372" x2="140" y2="372"/>

    <rect class="wrap-red" x="20" y="408" width="320" height="96"/>
    <text class="market-label" font-size="34">
      <tspan x="38" y="448">Residential &amp;</tspan>
      <tspan x="38" y="488">Commercial</tspan>
    </text>

    <text class="phone" x="40" y="580" font-size="38">(555) 014-2293</text>
    <text class="web-address" x="42" y="608" font-size="17">rjheatingandcooling.com</text>

    <rect x="370" y="290" width="240" height="400" rx="24" fill="url(#mascotTones)" role="img" aria-label="Cartoon HVAC technician mascot holding a pipe wrench"/>
  </svg>

</main>
</body>
</html>
```